Letterhead and Business card for Construction company

We need a letterhead and business card with our new company logo. We are based in NY. We develop and build properties.

The design should incorporate some unique feature from the logo (shape, font...). it should look like an extension from it.

Design should be clean and elegant, professional, not too busy.

The letterhead should include:
Logo (attached)
Address
Phone
Email

Please find the attached logo images and AI file.

Target Market(s)

Construction industry professionals

Industry/Entity Type

Construction, Development

Font styles to use
Sans Serif

Colors

Designer to choose colors to be used in the design.

Requirements
Must have
• Design should incorporate logo elements, additional assets are welcome. I'd like to see some other shapes / images invorporated too.

```html
<!DOCTYPE html>
<html lang="en">
<head>
<meta charset="utf-8">
<title>Korvane Builders – Business Card</title>
<link rel="stylesheet" href="https://fonts.googleapis.com/css2?family=Roboto:wght@400;500;700&display=swap">
<style>
  :root {
    --orange: #f47f20;
    --ink: #0b0b0b;
    --paper: #ffffff;
    --backdrop: #a9a7a8;
    --muted: #333333;
  }
  * { box-sizing: border-box; margin: 0; padding: 0; }
  html, body {
    width: 1200px; height: 900px; overflow: hidden;
    background: var(--backdrop);
    font-family: "Roboto", Arial, sans-serif;
  }
  .sheet { position: relative; width: 1200px; height: 900px; }

  .card {
    position: absolute;
    width: 525px; height: 300px;
    top: 300px;
    overflow: hidden;
  }
  .card--front { left: 50px; background: var(--paper); }
  .card--back  { left: 625px; background: var(--orange); }

  /* front */
  .brand-name {
    position: absolute; left: 32px; top: 34px;
    font-weight: 700; font-size: 30px; line-height: 1;
    color: var(--ink); letter-spacing: 1px;
  }
  .brand-name small { display: block; font-size: 16px; letter-spacing: 4px; margin-top: 6px; font-weight: 700; }
  .address {
    position: absolute; left: 34px; top: 104px;
    font-size: 12px; line-height: 1.45; color: var(--muted);
  }
  .contact-band {
    position: absolute; left: 0; top: 172px;
    width: 265px; height: 128px;
    background: var(--orange);
  }
  .contact-list {
    list-style: none;
    position: absolute; left: 24px; top: 16px;
    color: var(--paper); font-size: 13px; line-height: 1.6;
  }
  .contact-list li { display: flex; align-items: center; gap: 8px; }
  .contact-list svg { width: 11px; height: 11px; flex: none; }
  .person {
    position: absolute; right: 36px; top: 118px; text-align: right;
  }
  .person__name { color: var(--orange); font-size: 19px; font-weight: 500; letter-spacing: .5px; }
  .person__role { color: var(--ink); font-size: 13px; margin-top: 4px; }
  .skyline {
    position: absolute; left: 265px; top: 172px;
    width: 260px; height: 128px;
    background: linear-gradient(135deg, var(--ink) 0%, #5a3410 50%, var(--ink) 100%);
  }

  /* back */
  .back-brand {
    position: absolute; left: 0; right: 0; top: 50%;
    transform: translateY(-50%);
    text-align: center; color: var(--paper);
    font-weight: 700; font-size: 46px; line-height: 1; letter-spacing: 2px;
  }
  .back-brand small { display: block; font-size: 22px; letter-spacing: 7px; margin-top: 10px; font-weight: 700; }
</style>
</head>
<body>
<main class="sheet">
  <section class="card card--front" aria-label="Business card front">
    <div class="brand-name">KORVANE<small>BUILDERS</small></div>
    <p class="address">Your address, city<br>state, ZIP 0000</p>

    <div class="person">
      <div class="person__name">DANIEL REYES</div>
      <div class="person__role">Manager</div>
    </div>

    <div class="contact-band">
      <ul class="contact-list">
        <li>
          <svg viewBox="0 0 12 12" aria-hidden="true"><path fill="#fff" d="M2.5 1 4.3 1 5 3.4 3.9 4.4a6.5 6.5 0 0 0 3.7 3.7L8.6 7 11 7.7V9.5C11 10.3 10.3 11 9.5 11 5 11 1 7 1 2.5 1 1.7 1.7 1 2.5 1Z"/></svg>
          555-014-7320
        </li>
        <li>
          <svg viewBox="0 0 12 12" aria-hidden="true"><rect x="1" y="2.5" width="10" height="7" fill="none" stroke="#fff" stroke-width="1.2"/><path d="M1 2.5 6 6.5 11 2.5" fill="none" stroke="#fff" stroke-width="1.2"/></svg>
          mail@korvanebuild.com
        </li>
        <li>
          <svg viewBox="0 0 12 12" aria-hidden="true"><circle cx="6" cy="6" r="5" fill="none" stroke="#fff" stroke-width="1.1"/><ellipse cx="6" cy="6" rx="2.2" ry="5" fill="none" stroke="#fff" stroke-width="1"/><path d="M1 6h10" stroke="#fff" stroke-width="1"/></svg>
          www.korvanebuild.com
        </li>
      </ul>
    </div>

    <div class="skyline" role="img" aria-label="Building skyline graphic in black and orange"></div>
  </section>

  <section class="card card--back" aria-label="Business card back">
    <div class="back-brand">KORVANE<small>BUILDERS</small></div>
  </section>
</main>
</body>
</html>
```